Website for an interior designer

We need a new website for Clara Beth Holloway whose new business name is Clara Beth Holloway Interiors. She is a residential interior designer with a mix of modern and contemporary tastes. We are in the process of overhauling her website which is +15 years old and not an accurate reflection of her tastes. The uploaded photos are from some of the houses she has done as well as her logo(s). We would need a section for "About Us" that would have a paragraph of text and bullets showing services and a gallery for photos (~12 total, more to come). A contract page would be optional. The client likes the feel/look of this website: https://www.pondrickstudio.example/ but doesn't want to copy it exactly.

Target Market(s)

Upscale home owners

Industry/Entity Type

Interior Design

Coding

Coded - Design and coding required

Number of Pages Required

4 page

Colors

Designer to choose only greyscale colors for use in the design.

Requirements
Must have
• Home page, about us page, gallery page, contact us page.

```html
<!DOCTYPE html>
<html lang="en">
<head>
<meta charset="utf-8">
<title>Clara Beth Holloway Interiors</title>
<link rel="stylesheet" href="https://fonts.googleapis.com/css2?family=Varela+Round&family=Nunito+Sans:wght@300;400&display=swap">
<style>
  :root {
    --ink: #3a3a3a;
    --ink-soft: #555555;
    --ink-muted: #6e6e6e;
    --rule: #2b2b2b;
    --card-border: #d4d4d4;
    --paper: #ffffff;
  }
  * { margin: 0; padding: 0; box-sizing: border-box; }
  h1, h2 { font-weight: 400; }
  html, body { width: 710px; height: 1200px; overflow: hidden; background: var(--paper); }
  body { position: relative; font-family: "Nunito Sans", sans-serif; color: var(--ink); }
  .abs { position: absolute; }

  .nav-link { position: absolute; top: 56px; font-family: "Varela Round", sans-serif; font-size: 7.2px; letter-spacing: 0.6px; color: var(--ink-soft); text-decoration: none; white-space: nowrap; }
  .brand { position: absolute; left: 255px; width: 200px; top: 26px; text-align: center; }
  .brand-dot { display: block; width: 14px; height: 14px; border-radius: 50%; background: var(--ink-soft); margin: 0 auto 11px; }
  .brand-name { display: block; font-family: "Varela Round", sans-serif; font-size: 8.6px; line-height: 12px; letter-spacing: 1px; color: var(--ink); text-transform: uppercase; }

  .hero { left: 29px; top: 93px; width: 658px; height: 280px;
    background: linear-gradient(100deg, #bfb39f 0%, #e4ddd0 30%, #ecebe5 55%, #d9d3c8 75%, #7b6e63 100%); }

  .section-title { position: absolute; left: 0; width: 710px; text-align: center; font-family: "Varela Round", sans-serif; font-size: 13.6px; line-height: 17px; color: var(--ink); }
  .title-rule { position: absolute; height: 1.2px; width: 25px; background: var(--rule); }

  .intro { left: 170px; width: 370px; top: 459px; text-align: center; font-weight: 300; font-size: 7.6px; line-height: 13.4px; color: var(--ink-soft); white-space: nowrap; }

  .service-card { position: absolute; width: 137px; height: 79px; border: 1px solid var(--card-border); padding: 17px 22px 0 18px; }
  .service-num { font-family: "Varela Round", sans-serif; font-size: 7.4px; color: var(--ink-muted); margin-bottom: 3px; }
  .service-name { font-family: "Varela Round", sans-serif; font-size: 7.7px; line-height: 9.3px; color: #222; }

  .works-title { left: 139px; top: 838px; font-family: "Varela Round", sans-serif; font-size: 13.6px; color: var(--ink); }
  .works-link { right: 139px; top: 852px; font-family: "Varela Round", sans-serif; font-size: 6.6px; color: var(--ink); text-decoration: none; }
  .work-tile { position: absolute; top: 880px; height: 197px; }
  .work-dining { left: 139px; width: 138px; background: linear-gradient(160deg, #d8d6d0 0%, #f1f0ec 45%, #b9b5ad 80%, #4a3f38 100%); }
  .work-lounge { left: 285px; width: 139px; background: linear-gradient(170deg, #c9c8c4 0%, #e3ded7 50%, #d6d3cf 100%); }
  .work-stair { left: 432px; width: 139px; background: linear-gradient(150deg, #e8d68a 0%, #d97758 45%, #e55a9a 75%, #c8409a 100%); }

  .footer-contact { left: 139px; top: 1134px; font-size: 7.2px; line-height: 12px; color: var(--ink-soft); text-transform: uppercase; white-space: nowrap; }
  .footer-copy { right: 139px; top: 1147px; font-size: 6.6px; color: var(--ink-soft); white-space: nowrap; }
</style>
</head>
<body>
  <header>
    <a class="nav-link" style="left:159px" href="#">HOME</a>
    <a class="nav-link" style="left:207px" href="#">ABOUT</a>
    <div class="brand">
      <span class="brand-dot"></span>
      <span class="brand-name">Clara Beth Holloway<br>Interiors</span>
    </div>
    <a class="nav-link" style="left:453px" href="#">GALLERY</a>
    <a class="nav-link" style="left:516px" href="#">CONTACT</a>
  </header>

  <div class="abs hero" role="img" aria-label="Bright living room with cream sofas, steel-framed glass doors and a dining table"></div>

  <h1 class="section-title" style="top:405px">We Are The Leader In The<br>Real Estate</h1>
  <span class="title-rule" style="left:342px; top:443px"></span>

  <p class="abs intro">
    Clara Beth Holloway has extensive experience in all aspects of interior design.<br>
    She has worked on a wide array of residential and commercial projects in her hometown of<br>
    Houston and across the United States.<br>
    Clara Beth's taste can best be described as a sophisticated blend of modern and traditional<br>
    styles that combine to create a clean, timeless space.
  </p>

  <h2 class="section-title" style="top:555px">What do we offer?</h2>
  <span class="title-rule" style="left:342px; top:577px"></span>

  <section>
    <div class="service-card" style="left:139px; top:611px"><div class="service-num">01/</div><div class="service-name">Concept Origination<br>&amp; Project Management</div></div>
    <div class="service-card" style="left:287px; top:611px"><div class="service-num">02/</div><div class="service-name">Review of Proposed Plans for New Construction and Remodels</div></div>
    <div class="service-card" style="left:435px; top:611px"><div class="service-num">03/</div><div class="service-name">Procurement of Furniture, Accents, Art, Fixtures and Fittings</div></div>
    <div class="service-card" style="left:139px; top:703px"><div class="service-num">04/</div><div class="service-name">Selection of Paints,<br>Finishes and Construction Materials</div></div>
    <div class="service-card" style="left:287px; top:703px"><div class="service-num">05/</div><div class="service-name">Vendor Coordination and Recommendations</div></div>
    <div class="service-card" style="left:435px; top:703px"><div class="service-num">06/</div><div class="service-name">Home Staging, Styling and Editing</div></div>
  </section>

  <h2 class="abs works-title">My Works</h2>
  <span class="title-rule" style="left:140px; top:858px"></span>
  <a class="abs works-link" href="#">View All Works &gt;</a>
  <div class="work-tile work-dining" role="img" aria-label="White dining room with brass pendant light and modern chairs"></div>
  <div class="work-tile work-lounge" role="img" aria-label="Curved cream sofa with round marble coffee table"></div>
  <div class="work-tile work-stair" role="img" aria-label="Staircase with a vivid multicolour runner beside yellow artwork"></div>

  <footer>
    <p class="abs footer-contact">418 Linden Crest Ave. Houston, TX 77019<br>Contact: +1 555 014 2276 / info@cbholloway.example</p>
    <p class="abs footer-copy">© 2020 CLARA BETH HOLLOWAY . All Rights Reserved</p>
  </footer>
</body>
</html>
```